Business Cards/Stationary for CIO Outsourcing Company
Velmora Solutions
Use same font as used in my logo
Dorian Halbrook
Partner
Four Maple Ridge Plaza
Suite 240
Harlow Springs, Texas 75091
dhalbrook@govelmora.com
www.govelmora.com
Logo icon can be shown separate from the name if necessary on stationary.

```html
<!DOCTYPE html>
<html lang="en">
<head>
<meta charset="utf-8">
<title>Velmora Solutions – Business Card</title>
<link rel="stylesheet" href="https://fonts.googleapis.com/css2?family=Noto+Serif:wght@400;700&display=swap">
<style>
  :root {
    --backdrop: #e4e4e4;
    --card: #ffffff;
    --brand-red: #b5121b;
    --ink-dark: #3a3a3a;
    --ink-soft: #5a5a5a;
    --divider: #d6d6d6;
  }
  html, body {
    margin: 0;
    padding: 0;
    width: 1200px;
    height: 871px;
    overflow: hidden;
    background: var(--backdrop);
  }
  .canvas {
    position: relative;
    width: 1200px;
    height: 871px;
  }
  .business-card {
    position: absolute;
    left: 100px;
    top: 150px;
    width: 1000px;
    height: 571px;
    background: var(--card);
    box-shadow: 0 6px 24px rgba(0,0,0,0.12);
    overflow: hidden;
    font-family: "Noto Serif", Georgia, serif;
  }
  .accent-band {
    position: absolute;
    left: 0;
    width: 1000px;
    height: 40px;
  }
  .accent-band--top { top: 0; }
  .accent-band--bottom { bottom: 0; }
  .brand-block {
    position: absolute;
    left: 0;
    top: 0;
    width: 340px;
    height: 571px;
    display: flex;
    flex-direction: column;
    align-items: center;
    justify-content: center;
    gap: 22px;
  }
  .brand-mark {
    width: 110px;
    height: 110px;
    border-radius: 50%;
    background: var(--brand-red);
  }
  .brand-name {
    margin: 0;
    font-size: 44px;
    font-weight: 400;
    letter-spacing: 3px;
    color: var(--brand-red);
  }
  .column-divider {
    position: absolute;
    left: 345px;
    top: 70px;
    width: 2px;
    height: 430px;
    background: var(--divider);
  }
  .contact-block {
    position: absolute;
    left: 385px;
    top: 70px;
    color: var(--ink-soft);
  }
  .person-name {
    margin: 0;
    font-size: 34px;
    font-weight: 400;
    color: var(--brand-red);
    line-height: 1.2;
  }
  .person-title {
    margin: 6px 0 40px;
    font-size: 22px;
    font-weight: 700;
    color: var(--ink-dark);
  }
  .address {
    margin: 0 0 22px;
    font-style: normal;
    font-size: 20px;
    line-height: 1.35;
  }
  .contact-list {
    list-style: none;
    margin: 0;
    padding: 0;
    font-size: 20px;
    line-height: 1.35;
  }
  .contact-list li {
    display: flex;
    align-items: center;
    gap: 14px;
  }
  .contact-icon {
    width: 14px;
    height: 14px;
    flex: none;
  }
</style>
</head>
<body>
<div class="canvas">
  <div class="business-card">
    <svg class="accent-band accent-band--top" viewBox="0 0 1000 40" aria-hidden="true">
      <path d="M345 0 H1000 V22 H370 Q345 22 345 0 Z" fill="var(--brand-red)"/>
    </svg>

    <div class="brand-block">
      <div class="brand-mark" aria-hidden="true"></div>
      <p class="brand-name">VELMORA</p>
    </div>

    <div class="column-divider"></div>

    <div class="contact-block">
      <h1 class="person-name">Dorian Halbrook</h1>
      <p class="person-title">Partner</p>
      <address class="address">
        Four Maple Ridge Plaza<br>
        Suite 240<br>
        Harlow Springs, Texas 75091
      </address>
      <ul class="contact-list">
        <li>
          <svg class="contact-icon" viewBox="0 0 14 14" aria-label="Phone"><rect x="3" y="0" width="8" height="14" rx="2" fill="var(--brand-red)"/><rect x="4.5" y="2" width="5" height="8" fill="#fff"/></svg>
          (555) 703-0147
        </li>
        <li>
          <svg class="contact-icon" viewBox="0 0 14 14" aria-label="Office phone"><path d="M2 4 Q7 0 12 4 L11 6 L9 5 L9 4 Q7 3 5 4 L5 5 L3 6 Z" fill="var(--brand-red)"/><rect x="3" y="7" width="8" height="6" rx="1" fill="var(--brand-red)"/></svg>
          (555) 664-0192
        </li>
        <li>
          <svg class="contact-icon" viewBox="0 0 14 14" aria-label="Email"><rect x="0" y="2" width="14" height="10" rx="1" fill="var(--brand-red)"/><path d="M1 3 L7 8 L13 3" stroke="#fff" stroke-width="1.4" fill="none"/></svg>
          dhalbrook@govelmora.com
        </li>
        <li>
          <svg class="contact-icon" viewBox="0 0 14 14" aria-label="Website"><circle cx="7" cy="7" r="6.5" fill="var(--brand-red)"/><path d="M1 7 H13 M7 1 Q3 7 7 13 M7 1 Q11 7 7 13" stroke="#fff" stroke-width="1" fill="none"/></svg>
          www.govelmora.com
        </li>
      </ul>
    </div>

    <svg class="accent-band accent-band--bottom" viewBox="0 0 1000 40" aria-hidden="true">
      <path d="M345 40 H1000 V18 H370 Q345 18 345 40 Z" fill="var(--brand-red)"/>
    </svg>
  </div>
</div>
</body>
</html>
```